Flyer Design

I need a flyer as Iam starting a business which cleans Leather couches,sofas,chairs for residential and businesses.
We clean the interiors of automobiles and marine craft, boats large and small.
We would like to be able to get across the message that we are affordable, personal and reliable.
The Gold coast is our market and within this area there is a large amount of holiday apartments and houses which do experience high traffic to their living and dinning areas.

Target Market(s)

Target market Home,Apartment,Marine and Auto Owners

Industry/Entity Type

Residential

Requirements
Must have
• The flyer must have Company name which is PURE HIDE RESTORE MOBILE NUMBER
0431759204
EMAIL tramkell@vornexmail.com
Colours would like bright Gold or green or Red eith black lettering very modern font
Nice to have
• I would like to keep it as simple and clean looking.but eye catching
Should not have
• Dont want the flyer to look like a Real Estate flyer or a pizza advertisement.

```html
<!DOCTYPE html>
<html lang="en">
<head>
<meta charset="utf-8">
<title>Pure Hide Restore – Flyer</title>
<link rel="stylesheet" href="https://fonts.googleapis.com/css2?family=PT+Sans:wght@400;700&family=Raleway:wght@200&display=swap">
<style>
  :root {
    --panel-grey: #c6c6c6;
    --ink-dark: #3b3b3b;
    --band-dark: #333333;
    --ring-white: #ffffff;
    --icon-white: #ffffff;
    --leather-highlight: #e39a5a;
    --leather-light: #cf7a3a;
    --leather-mid: #b0602c;
    --leather-shadow: #7a3f1e;
    --leather-deep: #3e2416;
    --text-white: #ffffff;
  }
  * { margin: 0; padding: 0; box-sizing: border-box; }
  html, body {
    width: 905px;
    height: 1200px;
    overflow: hidden;
    background: #ffffff;
  }
  .flyer {
    position: relative;
    width: 905px;
    height: 1200px;
    overflow: hidden;
    font-family: "PT Sans", Arial, sans-serif;
    color: var(--ink-dark);
  }
  .header-panel {
    position: absolute;
    left: 0; top: 0;
    width: 905px; height: 478px;
    background: var(--panel-grey);
  }
  .brand {
    position: absolute;
    left: 62px; top: 96px;
    display: flex;
    align-items: flex-start;
    gap: 10px;
  }
  .brand-square {
    width: 14px; height: 14px;
    margin-top: 10px;
    background: var(--ink-dark);
  }
  .brand-name {
    font-family: "Raleway", "Helvetica Neue", sans-serif;
    font-weight: 200;
    font-size: 34px;
    line-height: 1.12;
    letter-spacing: 1px;
    color: var(--ink-dark);
  }
  .headline {
    position: absolute;
    left: 300px; top: 96px;
    display: flex;
    align-items: center;
    gap: 22px;
  }
  .headline-text {
    font-size: 70px;
    font-weight: 400;
    line-height: 1;
    letter-spacing: 1px;
    color: var(--ink-dark);
  }
  .hide-mark {
    width: 84px; height: 66px;
    background: var(--ink-dark);
    border-radius: 18px;
  }
  .services-line {
    position: absolute;
    left: 300px; top: 190px;
    font-size: 16px;
    line-height: 1.35;
    color: var(--ink-dark);
  }
  .rule-right {
    position: absolute;
    left: 300px; right: 0; top: 250px;
    height: 2px;
    background: var(--ink-dark);
  }
  .rule-left {
    position: absolute;
    left: 0; top: 262px;
    width: 46px; height: 2px;
    background: var(--ink-dark);
  }
  .divider-band {
    position: absolute;
    left: 0; top: 462px;
    width: 905px; height: 22px;
    background: var(--band-dark);
  }
  .leather-photo {
    position: absolute;
    left: 0; top: 484px;
    width: 905px; height: 716px;
    background:
      radial-gradient(ellipse 55% 22% at 45% 20%, var(--leather-highlight), transparent 75%),
      radial-gradient(ellipse 90% 30% at 60% 52%, var(--leather-shadow), transparent 70%),
      radial-gradient(ellipse 45% 40% at 85% 75%, var(--leather-light), transparent 70%),
      linear-gradient(180deg, var(--leather-mid) 0%, var(--leather-light) 30%, #a3552a 60%, var(--leather-deep) 100%);
  }
  .service-icons {
    position: absolute;
    left: 0; top: 398px;
    width: 905px; height: 156px;
  }
  .service-icon {
    position: absolute;
    top: 0;
    width: 156px; height: 156px;
    border-radius: 50%;
    background: var(--ink-dark);
    border: 8px solid var(--ring-white);
    display: flex;
    align-items: center;
    justify-content: center;
  }
  .service-icon svg { width: 84px; height: 60px; fill: var(--icon-white); }
  .service-icon.couch { left: 174px; }
  .service-icon.boat  { left: 367px; }
  .service-icon.car   { left: 557px; }
  .contact {
    position: absolute;
    left: 96px; top: 1052px;
    color: var(--text-white);
  }
  .contact-phone {
    font-weight: 700;
    font-size: 32px;
    line-height: 1.25;
  }
  .contact-email {
    font-weight: 400;
    font-size: 31px;
    line-height: 1.25;
  }
</style>
</head>
<body>
<main class="flyer">
  <section class="header-panel">
    <div class="brand">
      <span class="brand-square"></span>
      <div class="brand-name">PURE<br>HIDE<br>RESTORE</div>
    </div>
    <div class="headline">
      <h1 class="headline-text">WE CLEAN</h1>
      <div class="hide-mark" role="img" aria-label="Leather hide symbol"></div>
    </div>
    <p class="services-line">Leather couches,sofas,chairs for residential and businesses,<br>the interiors of automobiles and marine craft, boats large and small.</p>
    <div class="rule-right"></div>
    <div class="rule-left"></div>
  </section>

  <div class="divider-band"></div>

  <div class="leather-photo" role="img" aria-label="Close-up photograph of a tan leather seat with stitched seam"></div>

  <div class="service-icons">
    <div class="service-icon couch" role="img" aria-label="Couch">
      <svg viewBox="0 0 84 60">
        <rect x="16" y="6" width="52" height="26" rx="6"/>
        <rect x="4" y="20" width="16" height="30" rx="6"/>
        <rect x="64" y="20" width="16" height="30" rx="6"/>
        <rect x="18" y="34" width="48" height="16" rx="3"/>
        <rect x="10" y="50" width="6" height="6"/>
        <rect x="68" y="50" width="6" height="6"/>
      </svg>
    </div>
    <div class="service-icon boat" role="img" aria-label="Boat">
      <svg viewBox="0 0 84 60">
        <polygon points="2,38 82,32 70,50 10,50"/>
        <polygon points="22,36 30,22 58,20 66,32"/>
        <polygon points="34,20 40,12 54,12 56,20"/>
      </svg>
    </div>
    <div class="service-icon car" role="img" aria-label="Car">
      <svg viewBox="0 0 84 60">
        <path d="M6 44 V32 L16 28 L28 14 H56 L70 28 L80 32 V44 Z"/>
        <circle cx="22" cy="46" r="8"/>
        <circle cx="64" cy="46" r="8"/>
      </svg>
    </div>
  </div>

  <section class="contact">
    <p class="contact-phone">Phone: 0431759204</p>
    <p class="contact-email">EMAIL tramkell@vornexmail.com</p>
  </section>
</main>
</body>
</html>
```